Business Name is TB Glamworks - Make-up Artist

I'm looking for an attractive and eye catching business card for for mobile make-up artist business. On the front of the card, I just want the name TB Glamworks in feminine type cursive writing and underneath my name Tessa Bourne and Make-Up Artist.
On the back of the card, I would like written down one side the following;
Make-Up Tutorials
Bridal
Photography
Debutante
Formals
Family Portraits
I would also like the following details as well as the Chatterbook and Pictoflow Icons;
Mobile: 0482 615 379
Email: tessabourne@maildrop-example.com
Website: tessabourne.velqora-example.com
Certificate III in Make-Up
Also, I would like a section that says Your Next Appointment and a space to put that information.
I would also like the Velqora Symbol on the bottom right hand corner (I have attached)

Target Market(s)

Mostly females

Industry/Entity Type

Makeup

Contact Information for Business Card

TB Glamworks
Tessa Bourne - Make-Up Artist

Font styles to use
Script

Colors
b768aa
886aae
e34297

Requirements
Must have
• Mobile: 0482 615 379
• Email: tessabourne@maildrop-example.com
• Website: tessabourne.velqora-example.com
• Certificate III in Make-Up
Nice to have
• Something to do with make-up like a smudged lipstick or some eye shadow
Should not have
• Don't want it too busy

```html
<!DOCTYPE html>
<html lang="en">
<head>
<meta charset="utf-8">
<title>TB Glamworks - Business Card</title>
<link rel="stylesheet" href="https://fonts.googleapis.com/css2?family=Quicksand:wght@400;500;700&display=swap">
<style>
  :root {
    --pink: #e34297;
    --violet: #6b3fae;
    --lilac: #886aae;
    --mauve: #b768aa;
    --ink: #5a3a9a;
    --paper: #ffffff;
    --backdrop: #e9e6ec;
  }
  * { box-sizing: border-box; margin: 0; padding: 0; }
  html, body { width: 1200px; height: 873px; overflow: hidden; }
  body {
    background: var(--backdrop);
    font-family: "Quicksand", sans-serif;
    display: flex;
    align-items: center;
    justify-content: center;
    gap: 80px;
  }
  .card {
    position: relative;
    width: 370px;
    height: 600px;
    background: var(--paper);
    box-shadow: 0 10px 30px rgba(60, 40, 80, 0.18);
    display: flex;
    flex-direction: column;
    align-items: center;
    overflow: hidden;
  }
  .brand-mark {
    position: absolute;
    top: 16px;
    right: 18px;
    color: var(--pink);
    font-size: 13px;
    font-weight: 500;
    letter-spacing: 0.5px;
  }
  .lip-print {
    width: 170px;
    height: 72px;
    margin-top: 62px;
    border-radius: 50% / 55%;
    background: linear-gradient(90deg, var(--lilac), var(--mauve) 55%, var(--pink));
    opacity: 0.85;
  }
  .business-name {
    margin-top: 14px;
    color: var(--pink);
    font-size: 38px;
    font-weight: 400;
  }
  .band {
    position: absolute;
    left: 0; right: 0; bottom: 0;
    height: 96px;
    background: linear-gradient(90deg, var(--violet), var(--lilac) 45%, var(--pink));
    display: flex;
    align-items: center;
    justify-content: space-around;
    padding: 0 20px;
  }
  .social {
    display: flex;
    align-items: center;
    gap: 6px;
    color: var(--paper);
    font-size: 12px;
    font-weight: 500;
  }
  .social::before {
    content: "";
    width: 14px; height: 14px;
    border-radius: 50%;
    background: var(--paper);
  }
  /* appointment side */
  .appointment {
    width: 290px;
    margin-top: 34px;
  }
  .appointment-title {
    color: var(--pink);
    font-size: 21px;
    font-weight: 400;
    text-align: center;
  }
  .weekdays {
    display: flex;
    justify-content: space-between;
    margin-top: 10px;
    color: var(--ink);
    font-size: 13px;
    font-weight: 500;
  }
  .entry-line {
    border-bottom: 2px dotted var(--pink);
    height: 30px;
  }
  .entry-label {
    color: var(--pink);
    font-size: 15px;
    margin-top: 8px;
  }
  /* details side */
  .person-name {
    margin-top: 26px;
    color: var(--ink);
    font-size: 26px;
    font-weight: 700;
  }
  .person-role {
    color: var(--pink);
    font-size: 18px;
    margin-top: 2px;
  }
  .contact-list {
    list-style: none;
    margin-top: 22px;
    width: 300px;
  }
  .contact-list li {
    display: flex;
    align-items: center;
    gap: 9px;
    color: var(--ink);
    font-size: 13.5px;
    line-height: 24px;
  }
  .contact-list svg { flex: none; width: 14px; height: 14px; }
  .qualification {
    margin-top: 22px;
    color: var(--pink);
    font-size: 15px;
    font-weight: 700;
  }
</style>
</head>
<body>

  <article class="card card--appointment">
    <span class="brand-mark">Velqora</span>
    <div class="lip-print" role="img" aria-label="Smudged lipstick kiss print in purple and pink"></div>
    <h1 class="business-name">TB Glamworks</h1>
    <section class="appointment">
      <h2 class="appointment-title">Your next appointment</h2>
      <div class="weekdays">
        <span>MON</span><span>TUE</span><span>WED</span><span>THU</span><span>FRI</span><span>SAT</span>
      </div>
      <div class="entry-line"></div>
      <div class="entry-line"></div>
      <p class="entry-label">DATE</p>
      <div class="entry-line" style="height:14px"></div>
      <p class="entry-label">TIME</p>
    </section>
    <footer class="band">
      <span class="social">Chatterbook</span>
      <span class="social">Pictoflow</span>
    </footer>
  </article>

  <article class="card card--details">
    <span class="brand-mark">Velqora</span>
    <div class="lip-print" role="img" aria-label="Smudged lipstick kiss print in purple and pink"></div>
    <h1 class="business-name">TB Glamworks</h1>
    <h2 class="person-name">Tessa Bourne</h2>
    <p class="person-role">Make-Up Artist</p>
    <ul class="contact-list">
      <li>
        <svg viewBox="0 0 16 16" fill="none" stroke="currentColor" stroke-width="1.5"><path d="M4 1.5l2.5 3-1.5 1.5c1 2 2.5 3.5 4.5 4.5L11 9l3 2.5-1.5 2.5C7 13.5 2.5 9 2 3.5z"/></svg>
        0482 615 379
      </li>
      <li>
        <svg viewBox="0 0 16 16" fill="none" stroke="currentColor" stroke-width="1.5"><rect x="1.5" y="3.5" width="13" height="9"/><path d="M1.5 3.5L8 9l6.5-5.5"/></svg>
        tessabourne@maildrop-example.com
      </li>
      <li>
        <svg viewBox="0 0 16 16" fill="none" stroke="currentColor" stroke-width="1.3"><circle cx="8" cy="8" r="6.5"/><ellipse cx="8" cy="8" rx="3" ry="6.5"/><path d="M1.5 8h13"/></svg>
        tessabourne.velqora-example.com
      </li>
    </ul>
    <p class="qualification">Certificate III in Make-Up</p>
    <footer class="band">
      <span class="social">Chatterbook</span>
      <span class="social">Pictoflow</span>
    </footer>
  </article>

</body>
</html>
```